Sports Flyer

Need a flyer for a kickball tournament

Kickball Tournament
Hosted by Tralvix (logo attached)

Information to include:
Tournament name: Harbor Lane Invitational
March 11th and 12th, 2023

Two days of events: COED (has advanced and social divisions) and WOMENS (advanced and social divisions)

Register at: www.tralvixhub.example

Address:
3817 Pelling Ridge Dr - Dunmore, NC 28412

Commentated by the "IRON PIKE SQUAD"

---

I have attached the mockup flyer that someone did for this tournament with the information on it, in addition to other examples of flyers. I want this one to look WAY better than anything I'm providing as reference.

Also attaching the images and logo.

I added three flyers that I found that I like as examples from online

```html
<!DOCTYPE html>
<html lang="en">
<head>
<meta charset="utf-8">
<title>Kickball Tournament – Harbor Lane Invitational</title>
<link href="https://fonts.googleapis.com/css2?family=Alfa+Slab+One&family=Roboto+Slab:wght@400;500;600;700;800&display=swap" rel="stylesheet">
<style>
  :root {
    --page-bg: #d9d9d9;
    --navy-deep: #0b2a5c;
    --navy: #123f85;
    --blue-glow: #2a7fd0;
    --field-dark: #0b2a33;
    --field-teal: #14605f;
    --gold-light: #fff3b8;
    --gold: #f2cc3f;
    --title-shadow: #101e4a;
    --white: #ffffff;
    --silver: #c9ced8;
    --ribbon-green: #7ec352;
    --accent-red: #e3262f;
    --pill-blue: #3a86c8;
    --address-gold: #f0c541;
    --photo-green: #4f8f3c;
    --photo-sky: #8fb8d8;
  }
  * { box-sizing: border-box; margin: 0; padding: 0; }
  html, body { width: 990px; height: 1200px; overflow: hidden; background: var(--page-bg); }
  body { position: relative; font-family: "Roboto Slab", serif; }

  .flyer {
    position: absolute; left: 31px; top: 0; width: 927px; height: 1200px; overflow: hidden;
    background:
      radial-gradient(ellipse 60% 30% at 50% 28%, rgba(60,150,230,.55), transparent 70%),
      radial-gradient(ellipse 70% 25% at 50% 62%, rgba(40,130,220,.45), transparent 70%),
      linear-gradient(180deg, var(--navy) 0%, #1a5aa8 35%, #16529c 60%, var(--navy-deep) 76%);
  }
  .field {
    position: absolute; left: 0; right: 0; top: 908px; bottom: 0;
    background:
      radial-gradient(ellipse 80% 40% at 50% 10%, rgba(40,150,130,.6), transparent 70%),
      linear-gradient(180deg, var(--field-teal) 0%, #0f4a4c 45%, var(--field-dark) 100%);
  }
  .field-edge {
    position: absolute; left: 0; right: 0; top: 900px; height: 10px;
    background: linear-gradient(90deg, #0a1a3a 0 8%, #1d5fa6 8% 30%, #153e78 30% 55%, #2a73c0 55% 80%, #153e78 80%);
  }
  .title {
    position: absolute; left: 0; right: 0; text-align: center;
    font-family: "Alfa Slab One", serif; line-height: 1; text-transform: uppercase;
    background: linear-gradient(180deg, var(--gold) 0%, var(--gold) 38%, var(--gold-light) 48%, var(--gold) 62%, #e8b92c 100%);
    -webkit-background-clip: text; background-clip: text; color: transparent;
    filter: drop-shadow(5px 5px 0 var(--title-shadow));
  }
  .title-kickball { top: 72px; font-size: 96px; letter-spacing: 2px; }
  .title-tournament { top: 186px; font-size: 96px; letter-spacing: 1px; }

  .action-photos { position: absolute; left: 71px; top: 327px; width: 785px; height: 311px; }

  .event-name {
    position: absolute; left: 0; right: 0; top: 675px; text-align: center;
    font-family: "Alfa Slab One", serif; font-size: 50px; line-height: 1; text-transform: uppercase;
    background: linear-gradient(180deg, var(--white) 0%, var(--white) 45%, var(--silver) 60%, var(--white) 100%);
    -webkit-background-clip: text; background-clip: text; color: transparent;
    filter: drop-shadow(4px 4px 0 var(--title-shadow));
  }
  .date-ribbon { position: absolute; left: 166px; top: 762px; width: 596px; height: 63px; }
  .date-ribbon svg { position: absolute; inset: 0; }
  .date-ribbon span {
    position: absolute; inset: 0; display: flex; align-items: center; justify-content: center;
    color: var(--white); font-weight: 700; font-size: 31px; letter-spacing: -.3px;
  }
  .events-heading {
    position: absolute; left: 0; right: 0; top: 840px; text-align: center;
    color: var(--accent-red); font-weight: 600; font-size: 27px; text-transform: uppercase;
  }
  .events-detail {
    position: absolute; left: 0; right: 0; top: 877px; text-align: center;
    color: var(--white); font-weight: 500; font-size: 16px;
  }
  .register {
    position: absolute; left: 97px; top: 917px; width: 732px; height: 53px;
    border-radius: 27px; overflow: hidden; display: flex; color: var(--white); font-weight: 600; font-size: 29px;
  }
  .register-label { width: 242px; background: var(--pill-blue); display: flex; align-items: center; justify-content: center; border-radius: 27px 0 0 27px; }
  .register-url { flex: 1; background: var(--accent-red); display: flex; align-items: center; justify-content: center; border-radius: 27px 27px 27px 27px; margin-left: -20px; }

  .address { position: absolute; left: 121px; top: 990px; color: var(--white); }
  .address-label { color: var(--address-gold); font-weight: 600; font-size: 29px; letter-spacing: 3px; text-transform: uppercase; margin-bottom: 8px; }
  .address-line { font-weight: 700; font-size: 30px; line-height: 39px; }
  .divider { position: absolute; left: 604px; top: 988px; width: 3px; height: 129px; background: var(--accent-red); }
  .host { position: absolute; left: 624px; width: 220px; top: 984px; text-align: center; color: var(--white); }
  .host-label { font-weight: 700; font-size: 20px; }
  .host-name { margin-top: 34px; display: flex; align-items: center; justify-content: center; gap: 10px; font-weight: 700; font-size: 34px; color: var(--white); }
  .host-name i { display: block; width: 18px; height: 18px; border-radius: 50%; background: var(--ribbon-green); }
  .commentary {
    position: absolute; left: 0; right: 0; top: 1139px; text-align: center;
    color: var(--white); font-weight: 600; font-size: 25px; letter-spacing: 5px; text-transform: uppercase;
  }
  .bottom-rule { position: absolute; left: 0; right: 0; bottom: 0; height: 6px; background: var(--accent-red); }
</style>
</head>
<body>
  <main class="flyer">
    <div class="field-edge"></div>
    <div class="field"></div>

    <h1 class="title title-kickball">Kickball</h1>
    <h1 class="title title-tournament">Tournament</h1>

    <svg class="action-photos" viewBox="0 0 785 311" role="img" aria-label="Four slanted photos of players catching and throwing kickballs on a turf field">
      <defs>
        <linearGradient id="turf" x1="0" y1="0" x2="0" y2="1">
          <stop offset="0" stop-color="var(--photo-sky)"/>
          <stop offset=".35" stop-color="#6e9a63"/>
          <stop offset="1" stop-color="var(--photo-green)"/>
        </linearGradient>
      </defs>
      <polygon points="0,0 207,0 137,311 0,311" fill="url(#turf)"/>
      <polygon points="219,0 414,0 346,311 149,311" fill="url(#turf)"/>
      <polygon points="426,0 625,0 556,311 358,311" fill="url(#turf)"/>
      <polygon points="637,0 785,0 785,311 568,311" fill="url(#turf)"/>
    </svg>

    <h2 class="event-name">Harbor Lane Invitational</h2>

    <div class="date-ribbon">
      <svg viewBox="0 0 596 63" preserveAspectRatio="none" aria-hidden="true">
        <polygon points="0,0 596,0 566,31.5 596,63 0,63 30,31.5" fill="var(--ribbon-green)"/>
      </svg>
      <span>MARCH 11TH AND 12TH, 2023</span>
    </div>

    <p class="events-heading">Two days of events:</p>
    <p class="events-detail">COED (has advanced and social divisions) and WOMENS (advanced and social divisions)</p>

    <div class="register">
      <div class="register-label">Register at:</div>
      <div class="register-url">www.tralvixhub.example</div>
    </div>

    <div class="address">
      <p class="address-label">Address:</p>
      <p class="address-line">3817 Pelling Ridge Dr -</p>
      <p class="address-line">Dunmore, NC 28412</p>
    </div>

    <div class="divider"></div>

    <div class="host">
      <p class="host-label">Hosted by</p>
      <p class="host-name"><i></i>Tralvix</p>
    </div>

    <p class="commentary">Commentated by the "Iron Pike Squad"</p>
    <div class="bottom-rule"></div>
  </main>
</body>
</html>
```